Lakemond Drywork Business Card Design

Professional and clean design. The design colors should flow with the logo. Two-sided card with the website on the back which is:

www.LakemondDrywork.example.

"Specializing in Water Damage Restoration"

On the front I need the name, email, phone, and logo.

Name: Darnell Quimby
Email: Darnell@LakemondDrywork.example
Phone: 555-018-2364 for now

I only have the Preview and Thumbnail right now but should have the source files uploaded within a day or two.

Target Market(s)

Flood victims, home owners with water damage from busted pipes etc...

Industry/Entity Type

Business

Contact Information for Business Card

Name: Darnell Quimby

Font styles to use
Serif
Sans Serif

Requirements
Must have
• Business Card Details Info

```html
<!DOCTYPE html>
<html lang="en">
<head>
<meta charset="utf-8">
<title>Lakemond Drywork Business Card</title>
<link rel="stylesheet" href="https://fonts.googleapis.com/css2?family=Cinzel:wght@400;500&family=PT+Sans:wght@400&display=swap">
<style>
  :root {
    --page: #eeeeee;
    --card: #ffffff;
    --brand-blue: #2e9bd6;
    --faint-blue: #d9eaf7;
    --ink: #3d3d3d;
    --ink-soft: #555555;
    --edge: #d8d8d8;
  }
  * { margin: 0; padding: 0; box-sizing: border-box; }
  html, body { width: 1200px; height: 379px; overflow: hidden; background: var(--page); }
  .canvas { position: relative; width: 1200px; height: 379px; }
  .card {
    position: absolute; top: 35px; width: 554px; height: 311px;
    background: var(--card); border: 1px solid var(--edge); overflow: hidden;
  }
  .card--front { left: 35px; }
  .card--back { left: 614px; }
  .card__decor { position: absolute; left: 0; top: 0; }

  .brand-mark {
    position: absolute; left: 126px; top: 6px; width: 60px; height: 60px;
    border-radius: 50%; background: var(--brand-blue);
  }
  .brand-name {
    position: absolute; font-family: "Cinzel", serif; font-weight: 500;
    color: var(--brand-blue); text-align: center; line-height: 1;
  }
  .card--front .brand-name { left: 14px; width: 284px; top: 78px; font-size: 29px; letter-spacing: 1px; }
  .card--front .brand-name span { display: block; margin-bottom: 4px; }
  .card--back .brand-name { left: 0; width: 552px; top: 112px; font-size: 38px; letter-spacing: 1px; padding-left: 120px; }

  .person { position: absolute; left: 26px; top: 145px; }
  .person__name { font-family: "Cinzel", serif; font-weight: 500; font-size: 19px; color: var(--brand-blue); letter-spacing: 0.5px; }
  .person__title { font-family: "Cinzel", serif; font-size: 15px; color: var(--ink); letter-spacing: 1.5px; margin-top: 2px; }

  .contact { position: absolute; left: 26px; top: 209px; list-style: none; font-family: "PT Sans", sans-serif; font-size: 13.5px; color: var(--ink); }
  .contact li { display: flex; align-items: center; height: 21.5px; }
  .contact svg { width: 11px; height: 11px; margin-right: 8px; fill: var(--ink-soft); }

  .tagline { position: absolute; left: 26px; top: 285px; font-family: "Cinzel", serif; font-size: 13px; color: var(--brand-blue); letter-spacing: 0.3px; }

  .website { position: absolute; left: 120px; width: 432px; top: 200px; text-align: center; font-family: "PT Sans", sans-serif; font-size: 16px; color: var(--ink); letter-spacing: 1px; }
</style>
</head>
<body>
<main class="canvas">
  <section class="card card--front" aria-label="Card front">
    <svg class="card__decor" width="554" height="311" aria-hidden="true">
      <circle cx="566" cy="151" r="150" fill="none" stroke="var(--faint-blue)" stroke-width="14"/>
    </svg>
    <div class="brand-mark" aria-hidden="true"></div>
    <div class="brand-name"><span>Lakemond</span><span>Drywork</span></div>
    <div class="person">
      <p class="person__name">Darnell Quimby</p>
      <p class="person__title">Title</p>
    </div>
    <ul class="contact">
      <li><svg viewBox="0 0 12 12"><path d="M2.5 0.5l2 2.2-1 1.3c.7 1.6 2 2.9 3.6 3.6l1.3-1 2.2 2-.9 2.3C5 10.5 1.2 6.8.3 1.4z"/></svg>555-018-2364</li>
      <li><svg viewBox="0 0 12 12"><path d="M0 2.5h12v7H0z M0.6 3l5.4 3.8L11.4 3" stroke="#fff" stroke-width="0.9"/></svg>Darnell@LakemondDrywork.example</li>
      <li><svg viewBox="0 0 12 12"><circle cx="6" cy="6" r="5.5"/><path d="M0.5 6h11M6 .5v11M2 3h8M2 9h8" stroke="#fff" stroke-width="0.7" fill="none"/></svg>www.LakemondDrywork.example</li>
    </ul>
    <p class="tagline">Specializing in Water Damage Restoration</p>
  </section>

  <section class="card card--back" aria-label="Card back">
    <svg class="card__decor" width="554" height="311" aria-hidden="true">
      <circle cx="-13" cy="151" r="150" fill="none" stroke="var(--faint-blue)" stroke-width="14"/>
    </svg>
    <div class="brand-name">Lakemond Drywork</div>
    <p class="website">www.LakemondDrywork.example</p>
  </section>
</main>
</body>
</html>
```